Stationery design for a hip Muslim Travel Agency

We are looking for a colorful and energetic stationery design for a Muslim tour and travel agency. We need a letterhead, A4 folder, business card and loyalty card design.

The designs should be clean and cheerful and have a feeling of a colorful mosaic in a mosque. You can use the Mingleroo avatar and cover photo as the basis.

Pelitaru card is a loyalty card we issue to our clients. This can have a similar feel to the business card and it should NOT have the word "card" added to the logo. Think of airline membership cards.

Target Market(s)

Indonesians, 25-44 years old, Muslim, interesting in Umroh and Haji and other Muslim tours.

Industry/Entity Type

Travel Agent

Contact Information for Business Card

As provided in the .psd file.

Font styles to use
Sans Serif

Colors
27a0d5
33b8a4
00a990
0492cd

Requirements
Must have
• Letterhead design
• A4 folder design
• Business card
• Loyalty card (without the word "card" in the logo)
Nice to have
• Use the mosaic patterns provided in the files. We want to express the theme of colorful Islam.
Should not have
• Don't copy the .psd files provided in the brief. This is just for the content, those files were not prepared by a designer.

```html
<!DOCTYPE html>
<html lang="en">
<head>
<meta charset="utf-8">
<title>Pelitaru Stationery</title>
<link rel="stylesheet" href="https://fonts.googleapis.com/css2?family=Quicksand:wght@500;700&family=Montserrat:wght@400;600&display=swap">
<style>
  :root {
    --stage: #3b3b3d;
    --teal: #33b8a4;
    --teal-deep: #00a990;
    --sky: #27a0d5;
    --blue: #0492cd;
    --lime: #8cc63f;
    --ink: #2b2b2b;
    --muted: #6d6d6d;
    --paper: #ffffff;
    --paper-shade: #ececec;
    --font-text: "Quicksand", sans-serif;
    --font-label: "Montserrat", sans-serif;
  }
  * { box-sizing: border-box; margin: 0; padding: 0; }
  html, body { width: 950px; height: 1200px; overflow: hidden; }
  body { background: var(--stage); position: relative; font-family: var(--font-text); color: var(--ink); }

  .piece { position: absolute; background: var(--paper); overflow: hidden; }
  .mosaic { position: absolute; left: 0; right: 0; background: linear-gradient(90deg, var(--blue), var(--sky) 40%, var(--teal) 60%, var(--blue)); }

  .brand { display: flex; align-items: center; gap: 5px; font-family: var(--font-text); font-weight: 700; color: var(--ink); white-space: nowrap; }
  .brand-mark { background: var(--teal); border-radius: 50%; flex: none; }
  .brand--light { color: #fff; }
  .brand--light .brand-mark { background: #fff; }

  /* Folder cover */
  .folder-cover { left: 66px; top: 50px; width: 234px; height: 420px; }
  .folder-cover svg { position: absolute; left: 0; top: 0; }
  .folder-cover .brand { position: absolute; left: 28px; top: 320px; font-size: 26px; }
  .folder-cover .brand-mark { width: 36px; height: 36px; }
  .folder-cover .mosaic { bottom: 0; height: 22px; }

  /* Folder inside */
  .folder-inside { left: 424px; top: 70px; width: 440px; height: 400px; background: transparent; overflow: visible; }
  .folder-panel { position: absolute; top: 0; width: 220px; height: 400px; background: linear-gradient(180deg, #fafafa, #eeeeee); }
  .folder-panel--left { left: 0; }
  .folder-panel--right { left: 220px; background: linear-gradient(180deg, #f0f0f0, #e4e4e4); }
  .folder-emboss { position: absolute; top: 90px; left: 0; right: 0; text-align: center; font-weight: 700; font-size: 24px; color: #dcdcdc; }
  .folder-pocket { position: absolute; left: 0; right: 0; bottom: 0; height: 118px; background: linear-gradient(180deg, #3cc2ad, var(--teal)); border-top-left-radius: 4px; border-top-right-radius: 4px; }
  .folder-pocket .brand { position: absolute; left: 40px; top: 34px; font-size: 24px; }
  .folder-pocket .brand-mark { width: 26px; height: 26px; }
  .folder-email { position: absolute; left: 60px; top: 86px; font-size: 7.5px; letter-spacing: 1.5px; color: #fff; }
  .pocket-card { position: absolute; left: 54px; top: 22px; width: 96px; height: 62px; background: #fff; box-shadow: 0 1px 3px rgba(0,0,0,.2); overflow: hidden; }
  .pocket-card .mosaic { height: 4px; }
  .pocket-card .brand { position: absolute; left: 6px; top: 26px; font-size: 7px; gap: 2px; }
  .pocket-card .brand-mark { width: 8px; height: 8px; }
  .pocket-card .pocket-lines { position: absolute; left: 50px; top: 14px; width: 40px; }
  .pocket-card .pocket-lines span { display: block; height: 2px; background: #c9c9c9; margin-bottom: 5px; }

  /* Letterhead */
  .letterhead { left: 37px; top: 560px; width: 381px; height: 520px; box-shadow: 0 2px 6px rgba(0,0,0,.35); }
  .letterhead > .mosaic { height: 18px; }
  .letterhead > .mosaic--top { top: 0; }
  .letterhead > .mosaic--bottom { bottom: 0; }
  .letterhead .brand { position: absolute; left: 24px; top: 60px; font-size: 21px; }
  .letterhead .brand-mark { width: 24px; height: 24px; }
  .contact-list { position: absolute; left: 254px; top: 44px; list-style: none; font-size: 5.2px; color: var(--muted); line-height: 1.25; }
  .contact-list li { display: flex; gap: 4px; margin-bottom: 3px; align-items: flex-start; }
  .contact-list .pair { gap: 12px; }
  .contact-list .pair span { display: flex; gap: 4px; }
  .icon { width: 6px; height: 6px; flex: none; }
  .dot { width: 5px; height: 5px; border-radius: 50%; background: var(--teal); flex: none; margin-top: .5px; }
  .letter-meta { position: absolute; left: 31px; top: 168px; font-size: 5.5px; color: var(--muted); line-height: 2.4; }
  .letter-date { position: absolute; right: 24px; top: 162px; font-size: 5.8px; color: var(--muted); }
  .letter-body { position: absolute; left: 31px; top: 214px; width: 319px; font-size: 5.3px; line-height: 1.8; color: var(--muted); text-align: justify; }
  .letter-body p { text-indent: 16px; margin-bottom: 9px; }
  .letter-sign { position: absolute; left: 31px; top: 378px; font-size: 5.3px; color: var(--muted); line-height: 1.4; }
  .signature { display: block; width: 48px; height: 14px; margin: 26px 0 4px; background: #e8e8e8; }

  /* Business card */
  .biz { top: 558px; width: 201px; height: 120px; }
  .biz .mosaic { height: 10px; }
  .biz .mosaic--top { top: 0; }
  .biz .mosaic--bottom { bottom: 0; }
  .biz-front { left: 502px; }
  .biz-front .brand { position: absolute; left: 10px; top: 52px; font-size: 12px; gap: 3px; }
  .biz-front .brand-mark { width: 14px; height: 14px; }
  .biz-divider { position: absolute; left: 100px; top: 18px; bottom: 18px; width: 1px; background: #dcdcdc; }
  .biz-person { position: absolute; left: 114px; top: 30px; font-size: 4.8px; color: var(--ink); }
  .biz-person strong { font-weight: 700; }
  .biz-role { display: block; color: var(--teal); font-style: italic; margin-top: 1px; }
  .biz-contacts { position: absolute; left: 114px; top: 58px; list-style: none; font-size: 3.6px; color: var(--muted); line-height: 1.3; }
  .biz-contacts li { display: flex; gap: 3px; margin-bottom: 4px; }
  .biz-contacts .dot { width: 4px; height: 4px; }
  .biz-back { left: 724px; }
  .biz-band { position: absolute; left: 0; right: 0; top: 40px; height: 40px; background: var(--teal); display: flex; align-items: center; justify-content: center; }
  .biz-band .brand { font-size: 15px; }
  .biz-band .brand-mark { width: 16px; height: 16px; }
  .piece-label { position: absolute; font-family: var(--font-label); font-size: 11.5px; color: #e8e8e8; letter-spacing: .3px; }

  /* Loyalty card */
  .loyal { left: 552px; width: 232px; height: 146px; }
  .loyal-front { top: 744px; }
  .loyal-services { position: absolute; left: 0; right: 0; top: 0; height: 96px; background: linear-gradient(180deg, #3dc4ae, var(--teal)); }
  .service { position: absolute; width: 50px; text-align: center; font-size: 3.3px; color: #fff; }
  .service-icon { width: 20px; height: 20px; margin: 0 auto 3px; border-radius: 50%; background: #fff; border: 1.5px solid #c8efe9; display: flex; align-items: center; justify-content: center; }
  .service-icon span { width: 8px; height: 8px; border-radius: 2px; background: var(--blue); }
  .service-icon .glyph-red { background: #e0413a; }
  .service-icon .glyph-dark { background: var(--ink); border-radius: 50%; }
  .service-icon .glyph-teal { background: var(--teal-deep); }
  .loyal-front .brand { position: absolute; left: 88px; top: 100px; font-size: 8px; gap: 3px; }
  .loyal-front .brand-mark { width: 9px; height: 9px; }
  .loyal-contacts { position: absolute; left: 0; right: 0; top: 113px; display: flex; justify-content: center; gap: 6px; font-size: 3.2px; color: var(--muted); }
  .loyal-contacts span { display: flex; align-items: center; gap: 1.5px; }
  .loyal-contacts .dot { width: 3px; height: 3px; margin: 0; }
  .loyal .mosaic { height: 10px; }
  .loyal .mosaic--top { top: 0; }
  .loyal .mosaic--bottom { bottom: 0; }
  .loyal-back { top: 918px; }
  .loyal-band { position: absolute; left: 0; right: 0; top: 46px; height: 56px; background: var(--teal); }
  .loyal-badge { position: absolute; left: 76px; top: 30px; width: 80px; height: 88px; border-radius: 50%; background: #fff; border: 3px solid #d3f1ec; display: flex; align-items: center; justify-content: center; }
  .loyal-badge .brand { flex-direction: column; gap: 4px; font-size: 12px; }
  .loyal-badge .brand-mark { width: 24px; height: 24px; }

  /* Logo lockup */
  .lockup { position: absolute; left: 568px; top: 1106px; font-size: 42px; gap: 14px; }
  .lockup .brand-mark { width: 54px; height: 54px; }
</style>
</head>
<body>

<!-- Folder cover -->
<section class="piece folder-cover" aria-label="Folder cover">
  <svg width="234" height="420" viewBox="0 0 234 420">
    <path d="M0,0 H180 C172,120 120,230 0,262 Z" fill="#e9b69a" role="img" aria-label="Photo of a suspension bridge at sunset over the water"/>
    <path d="M188,0 C182,125 125,238 0,270" fill="none" stroke="#0492cd" stroke-width="11"/>
    <path d="M206,0 C198,135 140,250 0,282" fill="none" stroke="#ffffff" stroke-width="7"/>
    <path d="M224,0 C215,145 160,262 6,292" fill="none" stroke="#00a990" stroke-width="5"/>
    <path d="M0,58 C8,30 20,12 34,0" fill="none" stroke="#00a990" stroke-width="5"/>
  </svg>
  <div class="brand"><span class="brand-mark"></span>pelitaru.id</div>
  <div class="mosaic" role="img" aria-label="Blue and teal mosque mosaic pattern"></div>
</section>

<!-- Folder inside spread -->
<section class="piece folder-inside" aria-label="Folder inside spread">
  <div class="folder-panel folder-panel--left">
    <div class="folder-emboss">pelitaru.id</div>
    <div class="folder-pocket">
      <div class="brand brand--light"><span class="brand-mark"></span>pelitaru.id</div>
      <div class="folder-email">rahmat@pelitaru.id</div>
    </div>
  </div>
  <div class="folder-panel folder-panel--right">
    <div class="folder-emboss">pelitaru.id</div>
    <div class="folder-pocket">
      <div class="pocket-card">
        <div class="mosaic" style="top:0" role="img" aria-label="Mosaic pattern"></div>
        <div class="brand"><span class="brand-mark"></span>pelitaru.id</div>
        <div class="pocket-lines"><span></span><span></span><span></span><span></span></div>
        <div class="mosaic" style="bottom:0" role="img" aria-label="Mosaic pattern"></div>
      </div>
    </div>
  </div>
</section>

<!-- Letterhead -->
<section class="piece letterhead" aria-label="Letterhead">
  <div class="mosaic mosaic--top" role="img" aria-label="Blue and teal mosque mosaic pattern"></div>
  <div class="brand"><span class="brand-mark"></span>pelitaru.id</div>
  <ul class="contact-list">
    <li><svg class="icon" viewBox="0 0 10 10"><path d="M5 0.5a3.3 3.3 0 0 1 3.3 3.3C8.3 6.5 5 9.5 5 9.5S1.7 6.5 1.7 3.8A3.3 3.3 0 0 1 5 .5z" fill="#33b8a4"/></svg><span>Jl. Melati Raya No. 14 Cempaka Barat<br>Kebon Asri, Jakarta Timur. 13820</span></li>
    <li><svg class="icon" viewBox="0 0 10 10"><circle cx="5" cy="5" r="5" fill="#33b8a4"/><path d="M3.3 2.6l1 1-.6.8c.4.8 1 1.4 1.8 1.8l.8-.6 1 1-.7.8C4.8 7.1 2.9 5.2 2.6 3.3z" fill="#fff"/></svg><span>0800-PELITARU (7354827)</span></li>
    <li><svg class="icon" viewBox="0 0 10 10"><circle cx="5" cy="5" r="5" fill="#33b8a4"/><rect x="2.3" y="3.2" width="5.4" height="3.6" fill="#fff"/><path d="M2.3 3.2L5 5.3l2.7-2.1" fill="none" stroke="#33b8a4" stroke-width=".6"/></svg><span>salam@pelitaru.id</span></li>
    <li class="pair"><span><i class="dot"></i>pelitaru.id</span><span><i class="dot"></i>Pelitaru</span></li>
    <li><i class="dot"></i><span>Pelitaru Indonesia</span></li>
  </ul>
  <div class="letter-date">Date: 21 Aug , 2018</div>
  <div class="letter-meta">Your Name Here<br>Address</div>
  <div class="letter-body">
    <p>Lorem ipsum dolor sit amet, consectetur adipiscing elit. Suspendisse condimentum egestas tellus et viverra. Vestibulum euismod lacus eget nisi ornare, id laoreet tortor dapibus. Donec lacinia euismod diam, convallis tempus risus. Ut et felis tempor eros blandit feugiat ut non enim. In vestibulum ligula blandit magna blandit dictum. Sed malesuada erat id mauris pretium, eget congue felis interdum. Aenean ultricies enim nec lorem vestibulum, nec commodo quam sagittis. Cras bibendum mauris eget aliquet semper, libero ipsum ultricies nunc, euismod pellentesque orci risus amet nibh. Maecenas feugiat mi a metus convallis pharetra.</p>
    <p>Duis porta turpis ut pulvinar hendrerit elit lorem vehicula turpis, lacinia semper purus ros ac nisi. Sed consectetur ante scelerisque tortor pellentesque imperdiet. Pellentesque habitant morbi tristique senectus et netus et malesuada fames ac turpis egestas. Quisque justo turpis, varius ante nec, tincidunt pharetra tellus. Donec non euismod est. Nulla in elit quis tellus mattis feugiat vitae vitae ut magna. Etiam at nisi quis dolor facilisis hendrerit placerat et risus. Vestibulum ac sapien ut justo varius venenatis.</p>
  </div>
  <div class="letter-sign">
    Regards
    <span class="signature" role="img" aria-label="Handwritten signature"></span>
    Your Name Here<br>Designation Here
  </div>
  <div class="mosaic mosaic--bottom" role="img" aria-label="Blue and teal mosque mosaic pattern"></div>
</section>

<!-- Business card front -->
<section class="piece biz biz-front" aria-label="Business card front">
  <div class="mosaic mosaic--top" role="img" aria-label="Mosaic pattern"></div>
  <div class="brand"><span class="brand-mark"></span>pelitaru.id</div>
  <div class="biz-divider"></div>
  <div class="biz-person"><strong>RAHMAT</strong> FAJAR WIBOWO<span class="biz-role">General Manager</span></div>
  <ul class="biz-contacts">
    <li><i class="dot"></i><span>Jl. Melati Raya No. 14 Cempaka Barat<br>Kebon Asri, Jakarta Timur. 13820</span></li>
    <li><i class="dot"></i><span>+62 8100 555 0192</span></li>
    <li><i class="dot"></i><span>rahmat@pelitaru.id</span></li>
  </ul>
  <div class="mosaic mosaic--bottom" role="img" aria-label="Mosaic pattern"></div>
</section>
<div class="piece-label" style="left:582px;top:687px">FRONT</div>

<!-- Business card back -->
<section class="piece biz biz-back" aria-label="Business card back">
  <div class="mosaic mosaic--top" role="img" aria-label="Mosaic pattern"></div>
  <div class="biz-band"><div class="brand brand--light"><span class="brand-mark"></span>pelitaru.id</div></div>
  <div class="mosaic mosaic--bottom" role="img" aria-label="Mosaic pattern"></div>
</section>
<div class="piece-label" style="left:807px;top:687px">BACK</div>

<!-- Loyalty card front -->
<section class="piece loyal loyal-front" aria-label="Loyalty card front">
  <div class="loyal-services">
    <div class="service" style="left:8px;top:12px"><div class="service-icon"><span class="glyph-dark"></span></div>VIP Airport Lounge</div>
    <div class="service" style="left:64px;top:12px"><div class="service-icon"><span></span></div>Passport &amp; Visa Service</div>
    <div class="service" style="left:120px;top:12px"><div class="service-icon"><span class="glyph-teal"></span></div>Onsite Manasik Service</div>
    <div class="service" style="left:176px;top:12px"><div class="service-icon"><span class="glyph-dark"></span></div>User ID Jamaah</div>
    <div class="service" style="left:36px;top:54px"><div class="service-icon"><span class="glyph-red"></span></div>Hajj &amp; Umrah Equipment</div>
    <div class="service" style="left:92px;top:54px"><div class="service-icon"><span class="glyph-dark"></span></div>Travel &amp; Life Insurance</div>
    <div class="service" style="left:148px;top:54px"><div class="service-icon"><span class="glyph-teal"></span></div>Meningitis Vaccine</div>
  </div>
  <div class="brand"><span class="brand-mark"></span>pelitaru.id</div>
  <div class="loyal-contacts">
    <span><i class="dot"></i>0800-PELITARU (7354827)</span>
    <span><i class="dot"></i>salam@pelitaru.id</span>
    <span><i class="dot"></i>pelitaru.id</span>
    <span><i class="dot"></i>Pelitaru</span>
    <span><i class="dot"></i>Pelitaru Indonesia</span>
  </div>
  <div class="mosaic mosaic--bottom" role="img" aria-label="Mosaic pattern"></div>
</section>
<div class="piece-label" style="left:798px;top:811px">LOYALTY CARD FRONT</div>

<!-- Loyalty card back -->
<section class="piece loyal loyal-back" aria-label="Loyalty card back">
  <div class="mosaic mosaic--top" role="img" aria-label="Mosaic pattern"></div>
  <div class="loyal-band"></div>
  <div class="loyal-badge"><div class="brand"><span class="brand-mark"></span>pelitaru.id</div></div>
  <div class="mosaic mosaic--bottom" role="img" aria-label="Mosaic pattern"></div>
</section>
<div class="piece-label" style="left:798px;top:984px">LOYALTY CARD BACK</div>

<!-- Logo lockup -->
<div class="brand brand--light lockup"><span class="brand-mark" style="background:var(--teal)"></span>pelitaru.id</div>

</body>
</html>
```